Brisket Dwelling Review is a leading provider of residential appraisal and home inspection products in S

I need a business card/logo designed that obviously describes my business. We are a residential appraisal and home inspection company in Springfield, MO. We offer residential appraisals, home inspection, pest inspection and radon gas measurement. We have been in business for 18 years and hold state certified residential appraisal licenses and VORMEL certified home inspection licenses. I have a logo that I really like and will attach, but would be open to new suggestions. I like more modern designs than traditional and would like a two sided card with our services, licenses and qualifications on the back.

```html
<!DOCTYPE html>
<html lang="en">
<head>
<meta charset="utf-8">
<title>Brisket Dwelling Review — Business Card</title>
<link href="https://fonts.googleapis.com/css2?family=Montserrat:wght@400;500;700;800&display=swap" rel="stylesheet">
<style>
  :root {
    --backdrop: #1e1e1f;
    --card: #ffffff;
    --orange: #f2a333;
    --brown: #a2825a;
    --logo-brown: #8a6a43;
    --ink: #6f6f6f;
    --icon: #8a8a8a;
  }
  * { margin: 0; padding: 0; box-sizing: border-box; }
  html, body { width: 1200px; height: 800px; overflow: hidden; }
  body {
    background: var(--backdrop);
    font-family: "Montserrat", Arial, sans-serif;
    display: flex;
    align-items: center;
    justify-content: center;
    gap: 48px;
  }
  .card {
    position: relative;
    width: 520px;
    height: 300px;
    background: var(--card);
    overflow: hidden;
  }

  /* Front */
  .card-front .brand {
    position: absolute;
    top: 0; left: 0; right: 0;
    height: 205px;
    display: flex;
    align-items: center;
    justify-content: center;
    gap: 12px;
  }
  .brand-mark {
    width: 20px; height: 20px;
    background: var(--orange);
  }
  .brand-name {
    font-weight: 800;
    font-size: 30px;
    color: var(--logo-brown);
    letter-spacing: -0.5px;
  }
  .card-front .stripe-brown {
    position: absolute; left: 0; right: 0;
    top: 212px; height: 10px;
    background: var(--brown);
  }
  .card-front .band-orange {
    position: absolute; left: 0; right: 0;
    top: 226px; bottom: 0;
    background: var(--orange);
  }

  /* Back */
  .card-back .band-orange {
    position: absolute; left: 0; right: 0;
    top: 0; height: 78px;
    background: var(--orange);
  }
  .card-back .stripe-brown {
    position: absolute; left: 0; right: 0;
    top: 82px; height: 9px;
    background: var(--brown);
  }
  .holder {
    position: absolute;
    left: 30px; top: 40px;
    display: flex; align-items: flex-end; gap: 12px;
    color: #fff;
  }
  .holder svg { width: 26px; height: 30px; }
  .holder-name { font-weight: 700; font-size: 17px; line-height: 1.05; }
  .holder-title { font-weight: 500; font-size: 13px; letter-spacing: 0.5px; }
  .contacts {
    position: absolute;
    left: 36px; top: 118px;
    list-style: none;
    display: flex; flex-direction: column; gap: 20px;
  }
  .contact {
    display: flex; align-items: center; gap: 20px;
    font-size: 13px; line-height: 1.3;
    color: var(--ink);
  }
  .contact svg { width: 20px; height: 22px; flex: none; }
</style>
</head>
<body>

  <section class="card card-front" aria-label="Card front">
    <div class="brand">
      <span class="brand-mark"></span>
      <span class="brand-name">Brisket Dwelling Review</span>
    </div>
    <div class="stripe-brown"></div>
    <div class="band-orange"></div>
  </section>

  <section class="card card-back" aria-label="Card back">
    <div class="band-orange"></div>
    <div class="stripe-brown"></div>

    <div class="holder">
      <svg viewBox="0 0 26 30" fill="none" stroke="#fff" stroke-width="2">
        <circle cx="13" cy="9" r="6"/>
        <path d="M2 29c0-7 5-11 11-11s11 4 11 11z"/>
      </svg>
      <div>
        <div class="holder-name">Mara Quill</div>
        <div class="holder-title">JOB TITLE</div>
      </div>
    </div>

    <ul class="contacts">
      <li class="contact">
        <svg viewBox="0 0 20 22" fill="none" stroke="var(--icon)" stroke-width="2">
          <rect x="4" y="1" width="12" height="20" rx="2"/>
          <line x1="8" y1="17" x2="12" y2="17"/>
        </svg>
        <span>Phone: 123 456 789<br>Office: 123 456 789</span>
      </li>
      <li class="contact">
        <svg viewBox="0 0 20 22" fill="none" stroke="var(--icon)" stroke-width="2">
          <rect x="1" y="9" width="10" height="6" rx="3" transform="rotate(-30 6 12)"/>
          <rect x="9" y="7" width="10" height="6" rx="3" transform="rotate(-30 14 10)"/>
        </svg>
        <span>maraquill@brisketdwelling.com<br>www.brisketdwelling.com</span>
      </li>
      <li class="contact">
        <svg viewBox="0 0 20 22" fill="var(--icon)">
          <path d="M10 1a7 7 0 0 0-7 7c0 5 7 13 7 13s7-8 7-13a7 7 0 0 0-7-7zm0 10a3 3 0 1 1 0-6 3 3 0 0 1 0 6z"/>
        </svg>
        <span>Address Line 1<br>Address Line 2</span>
      </li>
    </ul>
  </section>

</body>
</html>
```